Road Construction Company needs business cards

We would like a new business card designed for our business.

We're a road construction company based in Qld, Australia.

Can the business card please have the following information on it.

Name: Brent Malvoy
Position: General Manager
Phone: 0471 592 304
Email: Brent.malvoy@quendix.com.au
Address: 87 Harrowgate Ave, Pindarra, QLD, 4000
Website: www.quendix.com.au

Visually we'd like the card to be professional and simple.

Attached is our logo.

Our website is www.quendix.com.au

Target Market(s)

Men aged 25-60

Contact Information for Business Card

As listed in project description

Font styles to use
Serif

Requirements
Must have
• Large logo on back of card

```html
<!DOCTYPE html>
<html lang="en">
<head>
<meta charset="utf-8">
<title>Quendix Business Card</title>
<link href="https://fonts.googleapis.com/css2?family=Montserrat:wght@400;600;700&display=swap" rel="stylesheet">
<style>
  :root {
    --backdrop: #e4e4e3;
    --card-white: #f6f6f6;
    --brand-blue: #0c56a4;
    --card-blue-dark: #053b86;
    --card-blue-light: #0d5fad;
    --ink-light: #ecedf1;
  }
  * { margin: 0; padding: 0; box-sizing: border-box; }
  html, body {
    width: 1200px;
    height: 1200px;
    overflow: hidden;
    background: var(--backdrop);
    font-family: "Montserrat", sans-serif;
  }
  .card {
    position: absolute;
    left: 234px;
    width: 730px;
    height: 417px;
    box-shadow: 0 10px 24px rgba(0,0,0,0.18);
  }
  .card-front {
    top: 160px;
    background: var(--card-white);
    display: flex;
    align-items: center;
    justify-content: center;
  }
  .card-back {
    top: 632px;
    background: linear-gradient(120deg, var(--card-blue-dark), var(--card-blue-light));
    color: var(--ink-light);
  }
  .brand-name {
    font-weight: 700;
    letter-spacing: 2px;
    line-height: 1;
  }
  .card-front .brand-name {
    color: var(--brand-blue);
    font-size: 78px;
    margin-top: -18px;
  }
  .card-back .brand-name {
    position: absolute;
    right: 48px;
    top: 46px;
    font-size: 46px;
    color: var(--ink-light);
  }
  .person {
    position: absolute;
    left: 50px;
    top: 205px;
  }
  .person-name {
    font-size: 30px;
    font-weight: 600;
    line-height: 1.1;
  }
  .person-title {
    font-size: 19px;
    font-weight: 400;
    margin-top: 8px;
    letter-spacing: 0.4px;
  }
  .contact-list {
    list-style: none;
    margin-top: 16px;
  }
  .contact-list li {
    display: flex;
    align-items: center;
    gap: 9px;
    font-size: 19px;
    line-height: 28px;
    letter-spacing: 0.3px;
  }
  .contact-list svg {
    width: 16px;
    height: 16px;
    fill: none;
    stroke: var(--ink-light);
    stroke-width: 1.8;
    flex: none;
  }
  .address {
    position: absolute;
    right: 48px;
    top: 313px;
    font-size: 19px;
    line-height: 28px;
    text-align: right;
    font-style: normal;
    letter-spacing: 0.3px;
  }
</style>
</head>
<body>
  <section class="card card-front">
    <div class="brand-name">QUENDIX</div>
  </section>

  <section class="card card-back">
    <div class="brand-name">QUENDIX</div>

    <div class="person">
      <h1 class="person-name">Brent Malvoy</h1>
      <p class="person-title">General Manager</p>
      <ul class="contact-list">
        <li>
          <svg viewBox="0 0 24 24" aria-hidden="true"><path d="M5 3h4l2 5-2.5 1.5a11 11 0 0 0 6 6L16 13l5 2v4a2 2 0 0 1-2 2A17 17 0 0 1 3 5a2 2 0 0 1 2-2z"/></svg>
          0471 592 304
        </li>
        <li>
          <svg viewBox="0 0 24 24" aria-hidden="true"><rect x="3" y="5" width="18" height="14" rx="1"/><path d="M3 6l9 7 9-7"/></svg>
          Brent.malvoy@quendix.com.au
        </li>
        <li>
          <svg viewBox="0 0 24 24" aria-hidden="true"><circle cx="12" cy="12" r="9"/><path d="M3 12h18M12 3c3 3 3 15 0 18M12 3c-3 3-3 15 0 18"/></svg>
          www.quendix.com.au
        </li>
      </ul>
    </div>

    <address class="address">87 Harrowgate Ave, Pindarra,<br>QLD, 4000</address>
  </section>
</body>
</html>
```